Agriculture business need a new packaging design

we need a new design for our existing product (lebanese Cucumber 1.2 kg). You can see our existing design in attached file(current design.pdf). we want to replace the current design with a new design. This product is for the supermarket and aims to increase sales. We want to give a fresh and natural impact on design. I have attached some samples from other companies for your reference. Also attached Dieline 260mm .......Pdf so you can design as per Dieline format.
Updates

Please design artwork to print on polythene bag please

Target Market(s)

Supermarket Customer

Industry/Entity Type

agriculture

Requirements
Must have
• fresh and natural impact, Also this is artwork design to print on polythene bag, not Label design
Nice to have
• colorful, attractive

```html
<!DOCTYPE html>
<html lang="en">
<head>
<meta charset="utf-8">
<title>Lebanese Cucumbers 1.2kg – Polythene Bag Artwork</title>
<link rel="stylesheet" href="https://fonts.googleapis.com/css2?family=Lobster&family=Montserrat:wght@700&family=Libre+Baskerville&display=swap">
<style>
  :root {
    --backdrop: #b9b9b9;
    --bag-white: #ffffff;
    --dieline: #6d6d6d;
    --vent-pink: #c9708f;
    --seal-teal: #3fb7b5;
    --panel-dark: #3f8f2b;
    --panel-light: #a6d167;
    --title-cream: #fff7d6;
    --weight-yellow: #f4d93a;
    --brand-blue: #1f6fb2;
    --badge-green: #1e7a3a;
    --badge-gold: #f2c230;
    --photo-green: #2f5d22;
    --leaf-green: #3d6f2a;
  }
  html, body {
    margin: 0;
    width: 1200px;
    height: 2492px;
    overflow: hidden;
    background: var(--backdrop);
  }
  .bag-artwork {
    display: block;
    width: 1200px;
    height: 2492px;
  }
  .brand-name {
    font-family: "Montserrat", sans-serif;
    font-weight: 700;
    font-size: 7.5px;
    fill: var(--brand-blue);
  }
  .product-title {
    font-family: "Lobster", cursive;
    font-size: 15px;
    fill: var(--title-cream);
  }
  .net-weight {
    font-family: "Libre Baskerville", serif;
    font-size: 8px;
    fill: var(--weight-yellow);
  }
  .picked-date {
    font-family: "Libre Baskerville", serif;
    font-size: 6px;
    fill: var(--title-cream);
  }
  .dieline { fill: none; stroke: var(--dieline); stroke-width: 0.6; }
  .vent { fill: none; stroke: var(--vent-pink); stroke-width: 0.6; }
  .seal-line { fill: none; stroke: var(--seal-teal); stroke-width: 1.8; }
  .handle-slot { fill: var(--bag-white); stroke: var(--dieline); stroke-width: 0.7; }
</style>
</head>
<body>
<svg class="bag-artwork" viewBox="0 0 300 623" xmlns="http://www.w3.org/2000/svg">
  <defs>
    <linearGradient id="panelGradient" x1="0" y1="0" x2="0" y2="1">
      <stop offset="0" stop-color="var(--panel-dark)"/>
      <stop offset="0.45" stop-color="var(--panel-light)"/>
      <stop offset="0.85" stop-color="var(--panel-light)" stop-opacity="0.75"/>
      <stop offset="1" stop-color="var(--panel-light)" stop-opacity="0"/>
    </linearGradient>
    <g id="vent-block">
      <circle class="vent" cx="0" cy="0" r="3.6"/>
      <circle class="vent" cx="20" cy="0" r="3.6"/>
      <circle class="vent" cx="40" cy="0" r="3.6"/>
    </g>
    <g id="seal-base">
      <rect x="42" y="33" width="216" height="62" fill="var(--bag-white)"/>
      <path class="seal-line" d="M44 98 Q44 88 56 88 L244 88 Q256 88 256 98"/>
    </g>
    <g id="seal-marks">
      <rect class="handle-slot" x="120" y="57" width="58" height="14" rx="7"/>
      <g class="brand-mark">
        <rect x="56" y="59" width="7" height="7" fill="var(--brand-blue)"/>
        <text class="brand-name" x="66" y="65.5">Northvale</text>
      </g>
      <rect class="certification-badge" x="201" y="52" width="43" height="21" fill="var(--bag-white)" stroke="var(--badge-green)" stroke-width="0.8"/>
      <rect x="204" y="55" width="11" height="15" fill="var(--badge-gold)"/>
      <rect x="218" y="58" width="22" height="9" fill="var(--badge-green)"/>
    </g>
  </defs>

  <!-- bag body with side gussets -->
  <path d="M42 33 H258 V245 L218 287 L258 330 V590 H42 V330 L82 287 L42 245 Z" fill="var(--bag-white)"/>
  <path class="dieline" d="M42 33 H258 V245 L218 287 L258 330 V590 H42 V330 L82 287 L42 245 Z"/>
  <path class="dieline" d="M48 100 V240 L90 287 L48 334 V520"/>
  <path class="dieline" d="M252 100 V240 L210 287 L252 334 V520"/>
  <path class="dieline" d="M54 104 V236 L98 287 L54 338 V516"/>
  <path class="dieline" d="M246 104 V236 L202 287 L246 338 V516"/>

  <!-- vent holes -->
  <g class="vent-pattern">
    <use href="#vent-block" x="65" y="146"/><use href="#vent-block" x="195" y="146"/>
    <use href="#vent-block" x="65" y="166"/><use href="#vent-block" x="195" y="166"/>
    <use href="#vent-block" x="65" y="187"/><use href="#vent-block" x="195" y="187"/>
    <use href="#vent-block" x="65" y="209"/><use href="#vent-block" x="195" y="209"/>
    <use href="#vent-block" x="65" y="231"/><use href="#vent-block" x="195" y="231"/>
    <use href="#vent-block" x="88" y="300"/><use href="#vent-block" x="172" y="300"/>
    <use href="#vent-block" x="88" y="321"/><use href="#vent-block" x="172" y="321"/>
    <use href="#vent-block" x="65" y="390"/><use href="#vent-block" x="195" y="390"/>
    <use href="#vent-block" x="65" y="411"/><use href="#vent-block" x="195" y="411"/>
    <use href="#vent-block" x="65" y="432"/><use href="#vent-block" x="195" y="432"/>
    <use href="#vent-block" x="65" y="453"/><use href="#vent-block" x="195" y="453"/>
    <use href="#vent-block" x="65" y="474"/><use href="#vent-block" x="195" y="474"/>
  </g>

  <!-- seal areas -->
  <use href="#seal-base"/>
  <use href="#seal-base" transform="rotate(180 150 311.5)"/>

  <!-- product panel -->
  <g class="product-panel">
    <rect x="114" y="40" width="76" height="215" fill="url(#panelGradient)"/>
    <text class="product-title" x="152" y="110" text-anchor="middle">Lebanese</text>
    <text class="product-title" x="152" y="128" text-anchor="middle">Cucumbers</text>
    <g role="img" aria-label="Photo of whole and sliced Lebanese cucumbers">
      <ellipse cx="152" cy="158" rx="30" ry="17" fill="var(--photo-green)"/>
    </g>
    <g role="img" aria-label="Illustration of cucumber leaves with a yellow flower">
      <rect x="125" y="185" width="54" height="14" rx="6" fill="var(--leaf-green)"/>
    </g>
    <text class="net-weight" x="152" y="212" text-anchor="middle">1.2kg</text>
    <text class="picked-date" x="152" y="232" text-anchor="middle">Picked on</text>
    <text class="picked-date" x="152" y="240" text-anchor="middle">26/11/22</text>
  </g>

  <!-- handle, brand and badge above the panel -->
  <use href="#seal-marks"/>
  <use href="#seal-marks" transform="rotate(180 150 311.5)"/>
</svg>
</body>
</html>
```